webpage design for www.lumivaleYOU.com

Hi-
I am creating a website about weight loss through healthy eating. The target audience is 80% women, of all races and ethnic backgrounds, in the 35-55 age range, all of whom are overweight and want to lose weight.
At first (which is where you come in), the website will be strictly informational, and products for sale will be added later.
Obviously not all of the following information can be incorporated into the design, but to give you some background, here is what I am doing.
First thing the site visitor needs to know is what the website is about. It’s about them, and how they can lose weight effectively. It’s only secondarily about me, and the w
ebsite must talk about me only from the point of view of how can I help them. It is your job to create a webpage where I can do just that. I have the content of this page ready to go, but I need you to create a beautiful, enticing, and effective framework to put it all in. You do not need to enter any copy except for the small amount noted below.
My clients are looking for a weight loss method or program that is effective, healthy, and long-lasting. This system addresses those needs. It's important for the clients to know that with the lumivaleYOU system, there is no hunger, no deprivation, no pills, no weighing foods or calorie counting, no special products to buy, among other things.
And not only does the weight come off, but there are other health benefits as well. The lumivaleYOU system can lower cholesterol, blood pressure, dependence on insulin for type 2 diabetics, reduce risk of heart disease and certain types of cancer, among other things-and this has been medically documented.
When I say "healthy eating", the focus of this program is on vegetables, fruits, and grains, with no added fat, but I do not want the main page to highlight that, since the whole notion of lots of veggies can scare people away. Pictures of fruits and veggies are fine. I'll introduce scary words like “vegan” and “no added fat” into the written materials and in the video, but there is no point in chasing people away too quickly!
The banner headline should have incorporated into it, in addition to the business name, the following: "Lose weight...improve your looks...improve your health...transform your life". You will need to choose a typeface and add this copy.
I would like to have a collage of healthy, happy, slender people of all ages (mostly women), in group and social settings-but not all exercising or doing yoga or jogging, since many of my target audience are couch potatoes (at least right now). If you do use any pictures of overweight people, they should be solitary, not part of a group, and definitely not looking happy!. I was thinking of having this only in the banner at top, but if you find a way to make the site attractive by adding a thin border with this as well, feel free.
Or, since I am not a design person by any stretch of the imagination, if you have another idea as to the banner design and the rest, I am certainly open to it.
In addition to the banner headline, I want a two-column design on the lower section, one being a narrower sidebar on the right, with a place for the customer to enter his/her name, and the following: Free video & eBook" "Why Meal Plans Fail, Keep Failing, And Always Will Fail-And How To Break Free Of Them", and they get this in exchange for entering their first and last name, and email address. I can link this to Quillpost later. I have a video widget, as well as a bunch more, in place, so you do not need to create or order those.
I will later add something to this section about no spam will be sent.
Below that in the same thinner column on the right should be an archives section, which you will need to create if the Wordpress theme doesn't have it already. This should be the same on all pages, except the single column pages, and since they will have sales pitches, should not have anything else.
The wider, main column I want to have three particular areas: One, is video. Two is text. Three is comments.
I will be using a LOT of video, but below each video I want to be able to place the text for the video (not everyone wants to watch a video), I want a static first page, but no comments section on the first page (I may want to add a comments section later, but not now).
The next page will be a basic "about me" page. This will be a video with text below in the main section, and will have the same enter your email info on the right side bar. No need to have "comments" below this. I've uploaded a picture of me, which should appear on this page, as well as on the main page.
Then will be a blog page, again the same layout: videos, which I can add to consecutively, with "comments" below, (which I can approve or disapprove before they get posted), with the offer in the right sidebar. Any videos will also show up in the archives section.
And a "recipes" page, video and text, plus comments section, with the email offer in the sidebar. These will show up as an archives section as well. I’ll add recipes and cooking videos later.
Then will be a "Products" page, which will for now be blank (I haven't created them yet), but with the email offer in the right side bar. No comments section to this one.
And a Contact Us page, no comments section either. I'll add the contact information later.
Across bottom of each page, perhaps in a somewhat contrasting color, will be a disclaimer, which I’ll need to be able to edit. This will be in small print, and should say something like, “This website expresses the opinions of the author, is intended for informational and educational purposes only, should not be construed as medical or dietary advice, and is not intended to be a substitute for same. Before changing diets, medications, or before undertaking a weight loss regimen, be sure to consult with your physician. This information is not intended to diagnose or treat any illness or health problems you may be experiencing, so kindly address your doctor with these concerns.” You can copy and paste this text.
Each page should also say “copyright 2014, Ned Porski”, which you will need to add.
Beyond that I will need single blank column pages which I will later make into landing, thank you, and so on pages. This will not be visible from the main page, though.

This will be done in Wordpress. I have the URL and the page is set up on Wordpress already, but I will need you to integrate the design into my Wordpress site when it is completed, so you will need a working knowledge of Wordpress. So the final winner will need to have the capability of coding the design and uploading it into my website and server. When you are done, it will be a complete and turnkey website, and all I have to do is add the copy and videos.

I am not particular as to a Wordpress theme, as long as it's an unpaid one, but if you find a paid one that you think is useable and needs to be paid for, let me know so I can check it out.
And I will need to be easily able to change and edit anything in the webpage on Wordpress at the end, after you are finished, with NO HTML, so any theme must be dummy friendly (I am the dummy, by the way!). (I have a basic familiarity with Wordpress, but none of HTML.)

Hopefully this gives you more than enough information to work with. Even though this page is a bit complicated, the actual website should be pretty simple looking, not busy or full of distractions, with only a few focal points.
Updates

Hi-information has been updated, I've changed my status to "committed", and I've uploaded a lot of pictures of fruit and veggies for you to use.  Thanks for your attention!
Ned

Target Market(s)

As stated above, "The target audience is 80% women, of all races and ethnic backgrounds, in the 35-55 age range, all of whom are overweight and want to lose weight."

Industry/Entity Type

Cooking

Font styles to use
Serif

Requirements
Must have
• The home page serves two purposes: one, to introduce the reader to the material, but two, and equally important, to build my email list. To that end, the opt in form on the right should say prominently, Free video & eBook" "Why Meal Plans Fail, Keep Failing, And Always Will Fail-And How To Break Free Of Them", and below that should be the opt in boxes.
The banner can be scrolling, to attract ATTENTION, should lead to the ACTION of watching the video, which will have in it a CALL TO ACTION of signing up for the hopefully compelling OFFER of the free ebook and video-and of course the newsletter. My purpose on page one is to directly address the question of "What's in it for me?", and then to deliver with the video and ebook offer.
I've uploaded a bunch of pictures of veggies and fruit-feel free to use them, as they are all mine.
Possibly a scrolling banner could be used with alternating pictures of happy, slender people alternating with pictures, and the captions of "lLose weight...improve your looks...improve your health...transform your life"

Emphasis should be on healthy eating, not on pounds lost or measuring one's waist or some such thing.

Banner headline should include: ""Lose weight...improve your looks...improve your health...transform your life"
Nice to have
Should not have
• Please avoid pictures of picture-perfect people, scales, and so on-I do not want this to be some generic, cookie-cutter weight loss web site. This is about weight loss from a different point of view-and I don't think this will come across in the webpage, but the concept will be introduced later. It's about weight loss as a byproduct of changing eating habits from unhealthy to healthy.

```html
<!DOCTYPE html>
<html lang="en">
<head>
<meta charset="utf-8">
<title>lumivaleYOU – Lose weight, transform your life</title>
<link rel="stylesheet" href="https://fonts.googleapis.com/css2?family=Dosis:wght@300;400;500&display=swap">
<style>
  :root {
    --maroon: #8c1048;
    --maroon-text: #8b1a4a;
    --brown: #8a5a3a;
    --tan-ring: #c89a7a;
    --band: #efe5de;
    --footer: #efe7e1;
    --body-text: #555555;
    --field: #dcaabd;
    --field-text: #7a1b45;
    --button: #f8efeb;
    --white: #ffffff;
    --player-frame: #d6d8dc;
    --player-dark: #1e1e1e;
  }
  * { box-sizing: border-box; margin: 0; padding: 0; }
  html, body { width: 758px; height: 1200px; overflow: hidden; background: var(--white); }
  body { position: relative; font-family: Arial, Helvetica, sans-serif; color: var(--body-text); }

  /* hero */
  .hero { position: absolute; left: 0; top: 0; width: 758px; height: 455px; }
  .hero-photo {
    position: absolute; inset: 0;
    background: linear-gradient(180deg, #ffffff 0%, #fbf6f1 45%, #f3e2c8 75%, #eccf9c 90%, #f6efe6 100%);
  }
  .brand { position: absolute; left: 26px; top: 17px; display: flex; align-items: center; gap: 7px; }
  .brand-mark { width: 24px; height: 24px; background: var(--brown); }
  .brand-name { font-family: "Dosis", sans-serif; font-weight: 400; font-size: 24px; color: var(--brown); letter-spacing: .2px; }
  .main-nav { position: absolute; right: 27px; top: 22px; font-family: "Dosis", sans-serif; font-size: 13.5px; color: var(--brown); }
  .main-nav a { color: inherit; text-decoration: none; }
  .main-nav .sep { margin: 0 6px; }
  .headline { position: absolute; left: 479px; top: 88px; }
  .headline h1 { font-family: "Dosis", sans-serif; font-weight: 300; font-size: 32px; color: var(--maroon-text); line-height: 1.05; letter-spacing: .5px; }
  .headline .sub { font-family: "Dosis", sans-serif; font-weight: 300; font-size: 14.5px; color: var(--brown); margin-top: 1px; }
  .headline .tag { font-family: "Dosis", sans-serif; font-weight: 400; font-size: 22px; color: var(--maroon-text); margin-top: 2px; }

  /* features */
  .features { position: absolute; left: 0; top: 455px; width: 758px; height: 255px; background: var(--band); border-top: 3px solid #e6d8cd; }
  .feature { position: absolute; top: 38px; width: 152px; }
  .feature-icon { width: 84px; height: 84px; border-radius: 50%; border: 2px solid var(--tan-ring); padding: 4px; margin: 0 auto; }
  .feature-icon span { display: flex; width: 100%; height: 100%; border-radius: 50%; background: var(--maroon); align-items: center; justify-content: center; }
  .feature h2 { font-family: "Dosis", sans-serif; font-weight: 400; font-size: 18px; color: var(--maroon-text); text-align: center; margin-top: 12px; }
  .feature p { font-size: 11px; line-height: 13px; color: var(--body-text); margin-top: 11px; }

  /* video column */
  .video-player { position: absolute; left: 26px; top: 753px; width: 327px; height: 242px; background: var(--player-frame); border-radius: 6px; padding: 6px; }
  .player-screen { position: relative; width: 100%; height: 100%; background: var(--player-dark); border-radius: 4px; padding: 8px 10px 0; }
  .player-frame-img { width: 100%; height: 180px;
    background: linear-gradient(135deg, #c9d2d4 0%, #e8ecec 40%, #b7c27d 70%, #e4a94a 100%); }
  .play-button { position: absolute; left: 140px; top: 73px; width: 64px; height: 64px; }
  .player-controls { display: flex; align-items: center; gap: 10px; height: 30px; font-size: 7.5px; color: #dddddd; }
  .progress { position: absolute; left: 10px; right: 10px; top: 190px; height: 3px; background: #555; }
  .progress::before { content: ""; position: absolute; left: -3px; top: -3px; width: 9px; height: 9px; border-radius: 50%; background: #eee; }
  .video-text { position: absolute; left: 26px; top: 1012px; width: 340px; font-size: 11px; line-height: 13px; color: #333; }
  .learn-more { position: absolute; left: 26px; top: 1065px; font-size: 11px; color: var(--maroon-text); text-decoration: none; }

  /* opt-in */
  .optin { position: absolute; left: 395px; top: 750px; width: 332px; height: 326px; background: var(--maroon); border-radius: 4px; padding: 22px 19px; }
  .optin h2 { font-family: "Dosis", sans-serif; font-weight: 300; font-size: 36px; color: var(--white); line-height: 1; }
  .optin .offer { font-family: "Dosis", sans-serif; font-weight: 300; font-size: 14.5px; line-height: 19px; color: var(--white); margin-top: 9px; }
  .optin .field { display: block; width: 285px; height: 29px; margin-top: 9px; background: var(--field); border: 0; border-radius: 3px; padding: 0 14px; font-family: "Dosis", sans-serif; font-size: 15px; color: var(--field-text); line-height: 29px; }
  .optin .field:first-of-type { margin-top: 25px; }
  .optin .subscribe { display: block; margin-top: 16px; width: 144px; height: 37px; background: var(--button); border: 0; border-radius: 3px; font-family: "Dosis", sans-serif; font-size: 16px; color: var(--maroon-text); }

  /* footer */
  .site-footer { position: absolute; left: 0; top: 1110px; width: 758px; height: 90px; background: var(--footer); }
  .footer-brand { position: absolute; left: 11px; top: 24px; display: flex; align-items: center; gap: 6px; }
  .footer-brand .brand-mark { width: 19px; height: 19px; }
  .footer-brand .brand-name { font-size: 18px; }
  .copyright { position: absolute; left: 11px; top: 53px; font-size: 8px; color: var(--brown); }
  .footer-nav { position: absolute; left: 257px; top: 22px; font-size: 11px; }
  .footer-nav a { color: var(--brown); text-decoration: none; margin-right: 7px; }
  .social { position: absolute; left: 642px; top: 19px; display: flex; gap: 12px; }
  .social span { width: 18px; height: 18px; }
  .like-row { position: absolute; left: 644px; top: 46px; display: flex; gap: 5px; }
  .like-row span { height: 14px; border: 1px solid #c9ccd6; background: #f4f5f8; border-radius: 2px; }
  .like-row .count { font-size: 8px; color: #444; padding: 0 3px; line-height: 12px; background: #fff; }
</style>
</head>
<body>

<header class="hero">
  <div class="hero-photo" role="img" aria-label="Hero photo: smiling woman behind a table of fresh fruit and vegetables"></div>
  <div class="brand"><span class="brand-mark"></span><span class="brand-name">lumivaleYOU</span></div>
  <nav class="main-nav">
    <a href="#">home</a><span class="sep">|</span><a href="#">about us</a><span class="sep">|</span><a href="#">what we do</a><span class="sep">|</span><a href="#">contact us</a>
  </nav>
  <div class="headline">
    <h1>LOSE WEIGHT...</h1>
    <p class="sub">improve your looks... improve your health...</p>
    <p class="tag">transform your life</p>
  </div>
</header>

<section class="features">
  <div class="feature" style="left:16px">
    <div class="feature-icon"><span>
      <svg width="44" height="40" viewBox="0 0 44 40" fill="none" stroke="#fff" stroke-width="2.5" stroke-linecap="round"><line x1="22" y1="4" x2="22" y2="36"/><line x1="6" y1="10" x2="38" y2="10"/><path d="M2 22 L6 10 L10 22 Z"/><path d="M34 22 L38 10 L42 22 Z"/><line x1="14" y1="36" x2="30" y2="36"/></svg>
    </span></div>
    <h2>balance diet</h2>
    <p>Lorem ipsum dolor sit amet, consectetuer adipiscing elit, sed diam nonummy nibh euismod tincidunt ut.</p>
  </div>
  <div class="feature" style="left:210px">
    <div class="feature-icon"><span>
      <svg width="40" height="40" viewBox="0 0 40 40" fill="#fff"><path d="M20 12 C12 6 4 12 6 22 C8 32 14 36 20 33 C26 36 32 32 34 22 C36 12 28 6 20 12 Z"/><path d="M20 12 C20 8 22 5 25 3" stroke="#fff" stroke-width="2.5" fill="none"/></svg>
    </span></div>
    <h2>healthy eating</h2>
    <p>Ut wisi enim ad minim veniam, quis nostrud exerci tation ullamcorper suscipit lobortis nisl ut aliquip ex ea.</p>
  </div>
  <div class="feature" style="left:397px">
    <div class="feature-icon"><span>
      <svg width="38" height="38" viewBox="0 0 38 38"><rect x="3" y="3" width="32" height="32" rx="6" fill="#fff"/><rect x="11" y="8" width="16" height="7" rx="2" fill="#8c1048"/></svg>
    </span></div>
    <h2>lose weight</h2>
    <p>Nam liber tempor cum soluta nobis eleifend option congue nihil imperdiet doming id quod mazim placerat facer.</p>
  </div>
  <div class="feature" style="left:589px">
    <div class="feature-icon"><span>
      <svg width="44" height="40" viewBox="0 0 44 40"><path d="M22 36 C8 26 3 18 6 10 C9 3 18 3 22 10 C26 3 35 3 38 10 C41 18 36 26 22 36 Z" fill="#fff"/><polyline points="4,20 14,20 18,12 22,28 26,16 29,20 40,20" fill="none" stroke="#8c1048" stroke-width="2.2"/></svg>
    </span></div>
    <h2>healthy living</h2>
    <p>Claritas est etiam processus dynamicus, qui sequitur mutationem consuetudium lectorum. Mirum est notare.</p>
  </div>
</section>

<main>
  <div class="video-player">
    <div class="player-screen">
      <div class="player-frame-img" role="img" aria-label="Video still: woman taking food from a well-stocked refrigerator"></div>
      <svg class="play-button" viewBox="0 0 64 64"><circle cx="32" cy="32" r="29" fill="rgba(255,255,255,.15)" stroke="#fff" stroke-width="4"/><path d="M25 19 L46 32 L25 45 Z" fill="#fff"/></svg>
      <div class="progress"></div>
      <div class="player-controls">
        <svg width="9" height="10"><rect x="0" y="0" width="3" height="10" fill="#ddd"/><rect x="6" y="0" width="3" height="10" fill="#ddd"/></svg>
        <svg width="14" height="10"><path d="M0 3 H3 L7 0 V10 L3 7 H0 Z" fill="#ddd"/><path d="M9 2 Q12 5 9 8" stroke="#ddd" fill="none"/></svg>
        <span>00:00 / 18:50</span>
        <span style="flex:1"></span>
        <svg width="9" height="9"><circle cx="4.5" cy="4.5" r="3.5" fill="none" stroke="#ddd" stroke-width="2"/></svg>
        <svg width="8" height="8"><circle cx="4" cy="4" r="4" fill="#ddd"/></svg>
        <svg width="13" height="8"><rect x="1" y="1" width="11" height="6" fill="none" stroke="#ddd" stroke-width="2"/></svg>
        <svg width="15" height="10"><rect x="1" y="1" width="13" height="8" fill="none" stroke="#ddd" stroke-width="1.5"/></svg>
        <svg width="11" height="10" fill="none" stroke="#ddd" stroke-width="1.5"><path d="M0 3 V0 H3 M8 0 H11 V3 M11 7 V10 H8 M3 10 H0 V7"/></svg>
      </div>
    </div>
  </div>
  <p class="video-text">Ut wisi enim ad minim veniam, quis nostrud exerci tation ullamcorper suscipit lobortis nisl ut aliquip ex ea commodo consequat. Duis autem vel eum iriure dolor in hendrerit in vulputate velit esse molestie.</p>
  <a class="learn-more" href="#">Learn more »</a>

  <aside class="optin">
    <h2>Free video &amp; eBook</h2>
    <p class="offer">Why Meal Plans Fail, Keep Failing, And Always Will Fail-And How To Break Free Of Them</p>
    <span class="field">first name</span>
    <span class="field">last name</span>
    <span class="field">email address</span>
    <button class="subscribe" type="button">SUBSCRIBE</button>
  </aside>
</main>

<footer class="site-footer">
  <div class="footer-brand"><span class="brand-mark"></span><span class="brand-name">lumivaleYOU</span></div>
  <p class="copyright">© 2014 LumivaleYou. All Rights Reserved</p>
  <nav class="footer-nav"><a href="#">Home</a><a href="#">About Us</a><a href="#">What We Do</a><a href="#">Contact Us</a><a href="#">Terms</a><a href="#">Privacy</a></nav>
  <div class="social">
    <span style="background:#2aa9e0"></span>
    <span style="background:#3b5998"></span>
    <span style="background:#c4302b"></span>
  </div>
  <div class="like-row"><span style="width:34px"></span><span class="count">303k</span></div>
</footer>

</body>
</html>
```